Waterproofing Adhesive company needs design for bucket

We need a design for our 20kg/15kg and 4 kg bucket, Our companys name is Tolvarex Co LLC based in Umm Al Quwain, United Arab Emirates . Our main business is into waterproofing paint and Adhesive manufacturing. We are looking for a creative design for our buckets and paper bags. The design have to be attractive, The color theme of our company is light orange and yellow. I have attached the company logo along with this.

Target Market(s)

B2b , construction companys
Maintenance company

Industry/Entity Type

Manufacturer

Requirements
Must have
• It must have the company logo
• a spcae in centre to write the different products names
Nice to have
• A attractive design for placing the bucket in retail shops

```html
<!DOCTYPE html>
<html lang="en">
<head>
<meta charset="utf-8">
<title>Tolvarex bucket label options</title>
<link href="https://fonts.googleapis.com/css2?family=Montserrat:wght@500;700&family=Nanum+Pen+Script&display=swap" rel="stylesheet">
<style>
  :root {
    --page: #ffffff;
    --ink-grey: #6e6e6e;
    --ink-dark: #3b3b3b;
    --rule: #6a6a6a;
    --silver-light: #fafafa;
    --silver-mid: #dedede;
    --yellow-deep: #eab308;
    --yellow-light: #ffe866;
    --orange: #f26b1d;
    --amber: #f0a000;
  }
  * { margin: 0; padding: 0; box-sizing: border-box; }
  html, body { width: 1200px; height: 1000px; overflow: hidden; background: var(--page); }
  .canvas { position: relative; width: 1200px; height: 1000px; }

  .option-number {
    position: absolute; top: 116px; width: 40px; margin-left: -20px; text-align: center;
    font: 500 34px/1 "Montserrat", sans-serif; color: var(--ink-grey);
  }

  .label {
    position: absolute; top: 360px; width: 332px; height: 366px; overflow: hidden;
    border: 1px solid #e2e2e2;
  }
  .label--silver { left: 154px; background: linear-gradient(90deg, var(--silver-mid), var(--silver-light) 45%, var(--silver-mid)); }
  .label--gold { left: 716px; background: linear-gradient(90deg, #f0f0f0, #ffffff 50%, #e4e4e4); }

  .label__hero { position: absolute; left: 0; top: 0; width: 100%; height: 255px; }
  .label--gold .label__hero { background: linear-gradient(90deg, var(--yellow-deep), var(--yellow-light) 45%, var(--yellow-deep)); }

  .label__art { position: absolute; left: 10px; top: 10px; width: 312px; height: 166px; border-radius: 6px; }
  .label--silver .label__art { background: linear-gradient(120deg, #8a8a8a 0%, var(--amber) 40%, var(--orange) 70%, #8a8a8a 100%); opacity: .85; }
  .label--gold .label__art { background: linear-gradient(120deg, #7a7a7a 0%, var(--amber) 40%, var(--orange) 70%, #7a7a7a 100%); opacity: .85; }

  .label__brand {
    position: absolute; left: 0; width: 100%; top: 180px; text-align: center;
    font: 700 54px/1 "Montserrat", sans-serif; letter-spacing: -1px;
  }
  .label--silver .label__brand { color: var(--ink-grey); }
  .label--gold .label__brand { color: var(--ink-dark); }

  .label__rule { position: absolute; left: 0; width: 100%; height: 1px; background: var(--rule); }
  .label__rule--top { top: 255px; }
  .label__rule--bottom { top: 324px; }

  .label__product {
    position: absolute; left: 0; width: 100%; top: 262px; text-align: center;
    font: 400 46px/1 "Nanum Pen Script", cursive; color: var(--ink-grey); letter-spacing: 2px;
  }

  .label__foot { position: absolute; left: 0; top: 324px; width: 100%; height: 42px; }
  .label--gold .label__foot { top: 325px; background: linear-gradient(90deg, var(--yellow-deep), var(--yellow-light) 50%, var(--yellow-deep)); }

  .label__volume {
    position: absolute; left: 16px; top: 12px;
    font: 500 16px/1 "Montserrat", sans-serif; color: var(--ink-grey);
  }
  .label--gold .label__volume { color: var(--ink-grey); }

  .label__maker {
    position: absolute; right: 14px; top: 12px; display: flex; align-items: center; gap: 4px;
    font: 700 9px/1 "Montserrat", sans-serif; color: var(--orange);
  }
  .label__maker-dot { width: 16px; height: 16px; border-radius: 50%; background: var(--orange); }
</style>
</head>
<body>
<main class="canvas">
  <div class="option-number" style="left:328px">1</div>
  <div class="option-number" style="left:886px">2</div>

  <section class="label label--silver">
    <div class="label__hero">
      <div class="label__art" role="img" aria-label="Illustration of two crossed paint brushes, grey handles with amber and orange bristles"></div>
      <div class="label__brand">Tolvarex</div>
    </div>
    <div class="label__rule label__rule--top"></div>
    <div class="label__product">product name</div>
    <div class="label__rule label__rule--bottom"></div>
    <div class="label__foot">
      <span class="label__volume">4 litre</span>
      <span class="label__maker"><span class="label__maker-dot"></span>Tolvarex</span>
    </div>
  </section>

  <section class="label label--gold">
    <div class="label__hero">
      <div class="label__art" role="img" aria-label="Illustration of two crossed paint brushes, grey handles with amber and orange bristles"></div>
      <div class="label__brand">Tolvarex</div>
    </div>
    <div class="label__product">product name</div>
    <div class="label__foot">
      <span class="label__volume">4 litre</span>
      <span class="label__maker"><span class="label__maker-dot"></span>Tolvarex</span>
    </div>
  </section>
</main>
</body>
</html>
```